Lanternfield Disability - Social Security Disability Attorneys

Our company is expanding to attract clients nationwide for our social security disability practice. We have a logo, but I am looking for a creative and elegant letterhead that projects an image of being technologically advanced but still professional enough for the legal field. I am looking for the "wow factor" combined with this is still professional enough for a law practice.

Requesting letterhead and business card design
Updates

Had to update and change the logo. The previous logo had a typo. Please send updates with the new logo for consideration. The letterhead and business cards should be professional enough to be used for a law firm. Thanks.

Industry/Entity Type

Law Practice, Law Firm, Healthcare Industry, Government

Colors

Designer to choose colors to be used in the design.

Requirements
Nice to have
• **Please create a vertical design for the business card**

```html
<!DOCTYPE html>
<html lang="en">
<head>
<meta charset="utf-8">
<title>Lanternfield Disability – Letterhead</title>
<link href="https://fonts.googleapis.com/css2?family=Tinos:wght@400&family=Open+Sans:wght@400;600&display=swap" rel="stylesheet">
<style>
  :root{
    --backdrop:#e6e7ea;
    --paper:#ffffff;
    --ink:#1d1d1d;
    --mist:#eeeff2;
    --rule:#8d8f94;
  }
  *{margin:0;padding:0;box-sizing:border-box}
  html,body{width:1200px;height:900px;overflow:hidden;background:var(--backdrop)}
  .letterhead{
    position:absolute;left:267px;top:20px;width:666px;height:860px;
    background:var(--paper);box-shadow:0 4px 18px rgba(0,0,0,.18);
    font-family:"Tinos","Times New Roman",serif;color:var(--ink);overflow:hidden;
  }
  .header-pattern{
    position:absolute;left:0;top:0;width:100%;height:150px;
    background:linear-gradient(180deg,var(--mist) 0%,var(--mist) 70%,var(--paper) 100%);
  }
  .brand{
    position:absolute;left:0;top:92px;width:100%;
    display:flex;justify-content:center;align-items:center;gap:8px;
  }
  .brand-mark{width:8px;height:8px;border-radius:50%;background:var(--ink)}
  .brand-name{color:var(--ink);font-size:18px;font-weight:400;line-height:20px}
  .recipient{position:absolute;left:140px;top:182px;font-size:11px;line-height:12.5px;display:flex;gap:26px}
  .recipient address{font-style:normal}
  .body{position:absolute;left:124px;top:270px;width:462px;font-size:11px;line-height:13.4px}
  .body p{margin-bottom:14px}
  .body .salutation{margin-bottom:12px}
  .body .closing{margin-bottom:0}
  .signature{width:140px;height:34px;margin-top:6px;background:linear-gradient(90deg,#dfe3f1,#eef0f7)}
  .footer-band{
    position:absolute;left:0;bottom:0;width:100%;height:120px;
    background:linear-gradient(180deg,var(--paper) 0%,var(--mist) 100%);
  }
  .contact{
    position:absolute;left:104px;top:746px;height:94px;padding-left:14px;border-left:1px solid var(--rule);
    font-family:"Open Sans",Arial,sans-serif;font-size:7.3px;line-height:12.5px;color:#222;
    text-transform:uppercase;font-style:normal;
  }
  .contact b{font-weight:600}
</style>
</head>
<body>
<main class="letterhead">
  <div class="header-pattern" role="img" aria-label="Faint repeating pattern of light grey motifs across the header"></div>
  <div class="brand">
    <span class="brand-mark"></span>
    <span class="brand-name">Lanternfield Disability</span>
  </div>

  <div class="recipient">
    <span>To:</span>
    <address>Mr./Mrs. Sample Client<br>218 Maple Row<br>New York<br>NY 10490</address>
  </div>

  <section class="body">
    <p class="salutation">Dear Customer,</p>
    <p>Lorem ipsum dolor sit amet, consetetur sadipscing elitr, sed diam nonumy eirmod tempor invidunt ut labore et dolore magna aliquyam erat, sed diam voluptua. At vero eos et accusam et justo duo dolores et ea rebum. Stet clita kasd gubergren, no sea takimata sanctus est Lorem ipsum dolor sit amet. Lorem ipsum dolor sit amet, consetetur sadipscing elitr, sed diam nonumy eirmod tempor invidunt ut labore et dolore magna aliquyam erat, sed diam voluptua. At vero eos et accusam et justo duo dolores et ea rebum. Stet clita kasd gubergren, no sea takimata sanctus est Lorem ipsum dolor sit amet. Lorem ipsum dolor sit amet, consetetur sadipscing elitr, sed diam nonumy eirmod tempor invidunt ut labore et dolore magna aliquyam erat, sed diam voluptua. At vero eos et accusam et justo duo dolores et ea rebum. Stet clita kasd gubergren, no sea takimata sanctus est Lorem ipsum dolor sit amet.</p>
    <p>Duis autem vel eum iriure dolor in hendrerit in vulputate velit esse molestie consequat, vel illum dolore eu feugiat nulla facilisis at vero eros et accumsan et iusto odio dignissim qui blandit praesent luptatum zzril delenit augue duis dolore te feugait nulla facilisi. Lorem ipsum dolor sit amet, consectetuer adipiscing elit, sed diam nonummy nibh euismod tincidunt ut laoreet dolore magna aliquam erat volutpat.</p>
    <p>Nam liber tempor cum soluta nobis eleifend option congue nihil imperdiet doming id quod mazim placerat facer possim assum. Lorem ipsum dolor sit amet, consectetuer adipiscing elit, sed diam nonummy nibh euismod tincidunt ut laoreet dolore magna aliquam erat volutpat. Ut wisi enim ad minim veniam, quis nostrud exerci tation ullamcorper suscipit lobortis nisl ut aliquip ex ea commodo consequat.</p>
    <p class="closing">Sincerely,</p>
    <div class="signature" role="img" aria-label="Handwritten signature in blue ink"></div>
  </section>

  <div class="footer-band"></div>
  <address class="contact">
    1742 Beacon Ridge<br>Marlow, GA 30912<br><b>P:</b> 555-210-4400<br><b>F:</b> 555-210-4433
  </address>
</main>
</body>
</html>
```